Dryer Vent Cleaning Postcard Design

We need a postcard design for Flue Wranglers, a company that specializes in dryer vent cleaning, repairs and upgrades. Dryer vents need periodic cleaning to avoid lint clogging, dryer malfunction, long dry times and even a house fire. This card will be sent to residential and businesses prospects to introduce them to our services and the importance of maintaining their dryer vents. Our website is @ fluewrangling.com and provides information about our services, photos of our work and our general color scheme (purple/orange). Final print size will be 5x7 horizontal.

Target Market(s)

homeowners and business owners (spas, salons, grooming, gyms, laundrymats, etc)

Requirements
Must have
• Reduce the risk of fire
shortened dry times
lower energy consumption
18000 dryer fires caused in the US per year
Nice to have
• Does your dryer take too long to dry?

```html
<!DOCTYPE html>
<html lang="en">
<head>
<meta charset="utf-8">
<title>Flue Wranglers Postcard</title>
<link rel="stylesheet" href="https://fonts.googleapis.com/css2?family=Raleway:wght@300;400;600;700&family=Arimo:wght@700&display=swap">
<style>
:root{
  --page:#e1e2e4;
  --purple:#463a6f;
  --purple-dark:#3c3162;
  --orange:#f0804a;
  --lavender:#d8d4e6;
  --white:#ffffff;
  --ink:#111111;
  --art-a:#8a7fae;
  --art-b:#b9a894;
}
*{box-sizing:border-box;margin:0;padding:0}
html,body{width:864px;height:1200px;overflow:hidden;background:var(--page)}
body{position:relative;font-family:"Raleway",sans-serif}
.card{position:absolute;left:102px;width:678px;height:485px;overflow:hidden;background:var(--purple)}
.card--front{top:58px}
.card--back{top:624px}
.card-bg{position:absolute;inset:0}
.side-label{position:absolute;font-family:"Arimo",sans-serif;font-weight:700;font-size:28px;color:var(--ink)}
.side-label--front{left:146px;top:550px}
.side-label--back{left:702px;top:1120px}
.art{position:absolute;border-radius:14px;background:linear-gradient(160deg,var(--art-b),var(--art-a));opacity:.85}
.services{position:absolute;left:158px;top:160px;list-style:none;color:var(--white);font-weight:600;font-size:26px;line-height:39px}
.services li{display:flex;align-items:center;gap:5px}
.services li::before{content:"";width:11px;height:11px;border-radius:50%;background:var(--orange);box-shadow:0 0 0 2px #f6b08c}
.call-box{position:absolute;left:138px;top:358px;width:227px;height:60px;background:var(--purple);border-radius:0 12px 0 0;color:var(--white);text-align:center;font-weight:600;box-shadow:0 8px 10px rgba(0,0,0,.2)}
.call-box .label{font-size:21px;line-height:24px;padding-top:3px}
.call-box .phone{font-size:29px;font-weight:700;line-height:32px}
.brand-name{position:absolute;font-family:"Raleway",sans-serif;font-weight:700;color:var(--purple);text-align:center}
.web-bar{position:absolute;left:200px;right:0;bottom:0;height:36px;background:linear-gradient(90deg,rgba(0,0,0,0),#000 55%);color:var(--white);font-size:22px;text-align:right;padding-right:20px;line-height:36px}
.fact-ribbon{position:absolute;left:246px;top:24px;width:384px;height:34px;background:#000;color:var(--white);font-family:"Arimo",sans-serif;font-weight:700;font-size:15.5px;line-height:34px;text-align:center}
.contact{position:absolute;left:0;top:240px;width:328px}
.contact .phone{height:50px;background:var(--purple);border-radius:0 6px 0 0;display:flex;align-items:center;justify-content:flex-end;gap:8px;padding-right:18px;color:var(--white);font-weight:700;font-size:34px}
.contact .email{height:27px;background:var(--orange);display:flex;align-items:center;justify-content:center;gap:6px;color:var(--white);font-size:14.5px;font-weight:600}
.benefits{position:absolute;left:34px;top:364px;list-style:none;color:var(--white);font-weight:400;font-size:24px;line-height:29px}
.benefits li{display:flex;align-items:center;gap:3px}
.question{position:absolute;left:401px;top:394px;color:var(--white);font-weight:700;font-size:24.5px;line-height:31px}
</style>
</head>
<body>

<section class="card card--front">
  <svg class="card-bg" viewBox="0 0 678 485" aria-hidden="true">
    <path d="M0,290 C60,340 160,360 260,350 L0,400Z" fill="var(--purple-dark)"/>
    <path d="M0,352 C140,330 280,322 420,312 C520,306 610,312 678,330 L678,485 L0,485Z" fill="var(--orange)"/>
    <path d="M0,374 C200,345 430,318 678,342 L678,485 L0,485Z" fill="var(--lavender)"/>
    <path d="M0,392 C210,366 440,340 678,366 L678,485 L0,485Z" fill="var(--white)"/>
  </svg>
  <div class="art" style="left:46px;top:10px;width:568px;height:132px" role="img" aria-label="Illustration: technician holding a vent brush rod beside a duct and front-loading dryer"></div>
  <ul class="services">
    <li>Dryer Vent Cleaning</li>
    <li>Dryer Vent Repair &amp; Installation</li>
  </ul>
  <div class="art" style="left:14px;top:190px;width:150px;height:282px" role="img" aria-label="Illustration: technician pushing a red vent-cleaning vacuum"></div>
  <div class="call-box"><div class="label">Call Now</div><div class="phone">336-555-0142</div></div>
  <div class="art" style="left:490px;top:246px;width:150px;height:132px;border-radius:50%" role="img" aria-label="Illustration: smiling technician with brush and backpack vacuum"></div>
  <div class="brand-name" style="left:430px;top:384px;width:230px;font-size:26px">Flue Wranglers</div>
  <div class="web-bar">www.fluewrangling.com</div>
</section>
<div class="side-label side-label--front">Front</div>

<section class="card card--back">
  <svg class="card-bg" viewBox="0 0 678 485" aria-hidden="true">
    <path d="M0,0 L520,0 C500,120 480,250 520,370 C470,380 430,378 400,360 C300,330 180,320 0,318Z" fill="var(--orange)"/>
    <path d="M0,0 L500,0 C480,120 460,250 500,362 C440,370 420,360 400,350 C300,318 180,310 0,306Z" fill="var(--lavender)"/>
    <path d="M0,0 L490,0 C470,120 452,250 490,355 C430,360 410,350 390,342 C300,312 180,300 0,298Z" fill="var(--white)"/>
    <path d="M510,0 L560,0 C540,120 520,250 560,385 L520,376 C490,250 500,120 510,0Z" fill="var(--orange)"/>
    <path d="M0,240 L80,240 C200,250 300,280 360,300 L0,300Z" fill="var(--lavender)" opacity=".6"/>
    <polygon points="222,36 252,36 252,60 222,60 236,48" fill="var(--orange)"/>
    <polygon points="624,36 654,36 640,48 654,60 624,60" fill="var(--orange)"/>
  </svg>
  <div class="fact-ribbon">18000 dryer fires caused in the US per year!</div>
  <div class="art" style="left:62px;top:24px;width:150px;height:150px;border-radius:50%" role="img" aria-label="Illustration: smiling technician with brush and backpack vacuum"></div>
  <div class="brand-name" style="left:18px;top:180px;width:228px;font-size:26px">Flue Wranglers</div>
  <div class="contact">
    <div class="phone">
      <svg width="30" height="30" viewBox="0 0 24 24" aria-hidden="true"><path d="M6.6 10.8a15.1 15.1 0 0 0 6.6 6.6l2.2-2.2c.3-.3.7-.4 1-.2 1.1.4 2.3.6 3.6.6.6 0 1 .4 1 1V20c0 .6-.4 1-1 1A17 17 0 0 1 3 4c0-.6.4-1 1-1h3.5c.6 0 1 .4 1 1 0 1.3.2 2.5.6 3.6.1.3 0 .7-.2 1z" fill="var(--orange)"/></svg>
      336-555-0142
    </div>
    <div class="email">
      <svg width="16" height="12" viewBox="0 0 16 12" aria-hidden="true"><rect x=".5" y=".5" width="15" height="11" fill="var(--white)"/><path d="M1 1l7 6 7-6" fill="none" stroke="var(--orange)" stroke-width="1.4"/></svg>
      office@fluewrangling.com
    </div>
  </div>
  <div class="art" style="left:342px;top:64px;width:308px;height:324px" role="img" aria-label="Illustration: technician with brush rod beside a dryer spilling lint"></div>
  <ul class="benefits">
    <li><svg width="24" height="20" viewBox="0 0 24 20" aria-hidden="true"><path d="M2 11l6 6L22 3" fill="none" stroke="var(--orange)" stroke-width="3.4" stroke-linecap="round"/></svg>Reduce the risk of fire</li>
    <li><svg width="24" height="20" viewBox="0 0 24 20" aria-hidden="true"><path d="M2 11l6 6L22 3" fill="none" stroke="var(--orange)" stroke-width="3.4" stroke-linecap="round"/></svg>Shortened dry times</li>
    <li><svg width="24" height="20" viewBox="0 0 24 20" aria-hidden="true"><path d="M2 11l6 6L22 3" fill="none" stroke="var(--orange)" stroke-width="3.4" stroke-linecap="round"/></svg>Lower energy consumption</li>
  </ul>
  <p class="question">Does your dryer take<br>too long to dry?</p>
</section>
<div class="side-label side-label--back">Back</div>

</body>
</html>
```